Modern business card design for professional copywriter

I'd like a business card design that I can use to have my cards printed out by plink.com as a squared corners business card (see artwork and design guidelines here: https://help.plink.com/hc/en-gb/sections/300481726-PLINK-Product-Templates)

The design should be clean and modern and reflect the colours, tone and branding on my website: https://noravestrel.com.au

Target Market(s)

Professionals, B2B small business owners

Industry/Entity Type

Business

Contact Information for Business Card

Nora Vestrel
m: 0427 593 864
e: nora@noravestrel.com.au
w: noravestrel.com.au

Font styles to use
Sans Serif

Requirements
Must have
• Tagline: "Smart copywriting for clever business people"
• Brand colours: fd8000, 009984, 666666 and black
Nice to have

```html
<!DOCTYPE html>
<html lang="en">
<head>
<meta charset="utf-8">
<title>Nora Vestrel – Business Card</title>
<link rel="stylesheet" href="https://fonts.googleapis.com/css2?family=Open+Sans:wght@600;700;800&display=swap">
<style>
  :root {
    --backdrop: #ececec;
    --card: #fdfcfa;
    --card-back: #ffffff;
    --orange: #f6a65b;
    --orange-deep: #f29a45;
    --orange-text: #f29a45;
    --teal-soft: #74b6a6;
    --teal-text: #17977f;
    --grey-text: #666666;
    --ink: #111111;
  }
  * { margin: 0; padding: 0; box-sizing: border-box; }
  html, body {
    width: 1200px;
    height: 1000px;
    overflow: hidden;
    background: var(--backdrop);
    font-family: "Open Sans", Arial, sans-serif;
  }
  .stage {
    position: relative;
    width: 1200px;
    height: 1000px;
  }
  .card {
    position: absolute;
    top: 341px;
    width: 520px;
    height: 317px;
    background: var(--card);
    overflow: hidden;
    box-shadow: 0 2px 10px rgba(0, 0, 0, 0.12);
  }
  .card--front { left: 60px; }
  .card--back { left: 620px; background: var(--card-back); }

  .corner-art {
    position: absolute;
    top: 0;
    right: 0;
    width: 170px;
    height: 200px;
    background: linear-gradient(200deg, var(--orange) 0%, var(--orange-deep) 100%);
  }

  .brand-name {
    position: absolute;
    left: 36px;
    top: 60px;
    font-size: 38px;
    font-weight: 600;
    color: var(--orange-text);
    letter-spacing: -0.5px;
    line-height: 1;
  }
  .tagline {
    position: absolute;
    left: 22px;
    top: 232px;
    font-size: 17px;
    font-weight: 700;
    color: var(--ink);
    letter-spacing: 5.2px;
    line-height: 31px;
    text-transform: uppercase;
  }

  .holder-name {
    position: absolute;
    left: 30px;
    top: 44px;
    font-size: 30px;
    font-weight: 800;
    color: var(--teal-text);
    letter-spacing: 4px;
    line-height: 1;
    text-transform: uppercase;
  }
  .contact-list {
    position: absolute;
    left: 26px;
    top: 234px;
    list-style: none;
    font-size: 11px;
    font-weight: 600;
    letter-spacing: 2px;
    line-height: 19px;
  }
  .contact-label {
    display: inline-block;
    width: 22px;
    color: var(--grey-text);
    font-weight: 800;
    text-transform: uppercase;
  }
  .contact-value {
    color: var(--orange-text);
    text-transform: uppercase;
  }
</style>
</head>
<body>
<main class="stage">

  <section class="card card--front" aria-label="Business card front">
    <div class="corner-art" role="img" aria-label="Decorative folded-paper corner artwork in orange, teal and grey"></div>
    <div class="brand-name">Nora Vestrel</div>
    <p class="tagline">Smart copywriting<br>for clever business people</p>
  </section>

  <section class="card card--back" aria-label="Business card back">
    <div class="corner-art" role="img" aria-label="Decorative folded-paper corner artwork in orange, teal and grey"></div>
    <h1 class="holder-name">Nora Vestrel</h1>
    <ul class="contact-list">
      <li><span class="contact-label">m:</span><span class="contact-value">0427 593 864</span></li>
      <li><span class="contact-label">e:</span><span class="contact-value">nora@noravestrel.com.au</span></li>
      <li><span class="contact-label">w:</span><span class="contact-value">noravestrel.com.au</span></li>
    </ul>
  </section>

</main>
</body>
</html>
```